Kestrel Gardenworks Business Card

An eye catching, yet simple business card that includes;

1. our logo
2. office phone - 5083172946
3. email - kestrelgardenworks@mailbrook.com
4. website - www.kestrelgardenworks.com
5. instagram - @kestrelgardenworksnv

```html
<!DOCTYPE html>
<html lang="en">
<head>
<meta charset="UTF-8">
<title>Kestrel Gardenworks Business Card</title>
<link rel="stylesheet" href="https://fonts.googleapis.com/css2?family=Lato:wght@400;700;900&display=swap">
<style>
  :root {
    --backdrop: #2a2d31;
    --card: #1c1716;
    --accent: #b8682a;
    --ink: #f1ede9;
    --ink-soft: #c9c3bd;
    --rule: #4a403b;
  }
  * { margin: 0; padding: 0; box-sizing: border-box; }
  html, body { width: 1200px; height: 952px; overflow: hidden; }
  body {
    background: var(--backdrop);
    font-family: "Lato", sans-serif;
    display: flex;
    flex-direction: column;
    align-items: center;
    justify-content: center;
    gap: 56px;
  }
  .card {
    position: relative;
    width: 640px;
    height: 366px;
    background: var(--card);
    overflow: hidden;
    box-shadow: 0 10px 30px rgba(0,0,0,.45);
  }
  .wordmark {
    display: flex;
    align-items: center;
    gap: 12px;
    color: var(--accent);
    font-weight: 900;
    text-transform: uppercase;
    letter-spacing: .04em;
    line-height: 1.05;
  }
  .wordmark .dot {
    flex: none;
    border-radius: 50%;
    background: var(--accent);
  }
  /* front */
  .card--front { display: flex; align-items: center; justify-content: center; }
  .card--front .wordmark { font-size: 38px; }
  .card--front .wordmark .dot { width: 26px; height: 26px; }

  /* back */
  .band { position: absolute; background: var(--accent); width: 14px; }
  .band--top { left: 0; top: 0; height: 140px; }
  .band--bottom { right: 0; bottom: 0; height: 140px; }
  .card--back .brand {
    position: absolute; left: 44px; top: 118px; width: 250px;
  }
  .card--back .wordmark { font-size: 24px; }
  .card--back .wordmark .dot { width: 18px; height: 18px; }
  .divider {
    position: absolute; left: 318px; top: 76px; width: 1px; height: 214px;
    background: var(--rule);
  }
  .handle {
    position: absolute; left: 44px; bottom: 46px;
    color: var(--ink-soft); font-size: 13px; letter-spacing: .02em;
  }
  .details { position: absolute; left: 346px; top: 110px; right: 30px; }
  .name {
    color: var(--accent); font-size: 21px; text-transform: uppercase;
    letter-spacing: .03em; font-weight: 400;
  }
  .name strong { font-weight: 900; }
  .role { color: var(--ink); font-size: 14px; margin-top: 4px; margin-bottom: 18px; }
  .contact { list-style: none; }
  .contact li {
    display: flex; align-items: center; gap: 8px;
    color: var(--ink); font-size: 13px; margin-bottom: 7px;
  }
  .contact svg { width: 12px; height: 12px; flex: none; fill: var(--accent); }
</style>
</head>
<body>
  <section class="card card--front">
    <div class="wordmark"><span class="dot"></span>Kestrel Gardenworks</div>
  </section>

  <section class="card card--back">
    <span class="band band--top"></span>
    <span class="band band--bottom"></span>
    <div class="brand">
      <div class="wordmark"><span class="dot"></span>Kestrel Gardenworks</div>
    </div>
    <p class="handle">@kestrelgardenworksnv</p>
    <span class="divider"></span>
    <div class="details">
      <h1 class="name">Daniel R. <strong>Whitcombe</strong></h1>
      <p class="role">Managing Director</p>
      <ul class="contact">
        <li>
          <svg viewBox="0 0 24 24"><path d="M6.6 10.8a15.1 15.1 0 0 0 6.6 6.6l2.2-2.2a1 1 0 0 1 1-.25 11.4 11.4 0 0 0 3.6.57 1 1 0 0 1 1 1V20a1 1 0 0 1-1 1A17 17 0 0 1 3 4a1 1 0 0 1 1-1h3.5a1 1 0 0 1 1 1c0 1.25.2 2.45.57 3.57a1 1 0 0 1-.25 1z"/></svg>
          5083172946
        </li>
        <li>
          <svg viewBox="0 0 24 24"><path d="M2 5h20v14H2z M2 5l10 8 10-8" fill="none" stroke="#b8682a" stroke-width="2.4"/></svg>
          kestrelgardenworks@mailbrook.com
        </li>
        <li>
          <svg viewBox="0 0 24 24"><circle cx="12" cy="12" r="9.5" fill="none" stroke="#b8682a" stroke-width="2.2"/><path d="M2.5 12h19M12 2.5c3 3 3 16 0 19M12 2.5c-3 3-3 16 0 19" fill="none" stroke="#b8682a" stroke-width="1.8"/></svg>
          www.kestrelgardenworks.com
        </li>
      </ul>
    </div>
  </section>
</body>
</html>
```